R4 Pips (CBD candy infused with Delta-8)

The proposed logo are two pool table balls. One is a D and the other is an 8, its a brand and we need a label for Gummy human treats. This treats are being infused with Delt-8. I i will upload examples only. The example is of the type of labels needed (package and label for bottle)

Target Market(s)

Your professionals

Font styles to use
Sans Serif

Requirements
Must have
• Youthful look
Nice to have
• Consider using the Delta symbol instead of the D.
Also, I provided a sample of a label that's used on two type of packages.

```html
<!DOCTYPE html>
<html lang="en">
<head>
<meta charset="utf-8">
<title>R4 Pips – CBD Gummies Label</title>
<link href="https://fonts.googleapis.com/css2?family=Montserrat:wght@700;800;900&family=Oswald:wght@500&display=swap" rel="stylesheet">
<style>
  :root {
    --page: #ffffff;
    --purple: #b57ddc;
    --purple-light: #dca6f2;
    --purple-deep: #a56cc9;
    --ink: #3b3b3b;
    --ring: #4a4a4a;
    --ice-1: #eaf4f8;
    --ice-2: #cfe3ea;
    --blue-1: #6fb6e8;
    --blue-2: #a9ddfb;
    --blue-bar: #8fcff5;
    --white: #ffffff;
  }
  * { box-sizing: border-box; margin: 0; padding: 0; }
  html, body { width: 1200px; height: 1200px; overflow: hidden; background: var(--page); }
  body { position: relative; font-family: "Montserrat", sans-serif; }

  .label {
    position: absolute; left: 170px; top: 70px;
    width: 860px; height: 1060px; overflow: hidden;
  }
  .top-band {
    position: absolute; left: 0; top: 0; width: 100%; height: 74px;
    background: linear-gradient(90deg, var(--purple-deep), var(--purple-light) 55%, var(--purple));
    display: flex; align-items: center; justify-content: center;
  }
  .tagline {
    color: var(--white); font-weight: 900; font-size: 21px; letter-spacing: 6px;
    padding-top: 18px;
  }
  .body-panel {
    position: absolute; left: 0; top: 74px; width: 100%; height: 682px;
    background: linear-gradient(135deg, var(--ice-2), var(--ice-1) 40%, var(--white) 60%, var(--ice-2));
    overflow: hidden;
  }
  .ring { position: absolute; left: 0; top: 0; }

  .brand {
    position: absolute; left: 0; width: 100%; top: 150px;
    display: flex; align-items: center; justify-content: center; gap: 18px;
  }
  .brand-dot { width: 54px; height: 54px; border-radius: 50%; background: var(--purple); }
  .brand-name { color: var(--purple); font-weight: 800; font-size: 66px; }

  .product-title {
    position: absolute; left: 0; width: 100%; text-align: center;
    color: var(--ink); font-weight: 900; line-height: 1;
  }
  .product-title.cbd { top: 318px; font-size: 142px; letter-spacing: 2px; }
  .product-title.gummies { top: 462px; font-size: 92px; }

  .infused-bar {
    position: absolute; left: 200px; top: 567px; width: 472px; height: 55px;
    background: var(--purple-light);
    color: var(--white); font-weight: 800; font-size: 40px;
    display: flex; align-items: center; justify-content: center;
  }
  .dose-bar {
    position: absolute; left: 200px; top: 627px; width: 472px; height: 32px;
    background: var(--blue-bar);
    color: var(--white); font-weight: 800; font-size: 22px;
    display: flex; align-items: center; justify-content: center;
  }

  .divider {
    position: absolute; left: 0; top: 756px; width: 100%; height: 18px;
    background: var(--purple);
  }
  .bottom-band {
    position: absolute; left: 0; top: 774px; width: 100%; height: 286px;
    background: linear-gradient(100deg, var(--blue-1), var(--blue-2) 50%, var(--blue-1));
  }
  .total {
    position: absolute; left: 0; width: 100%; text-align: center; top: 18px;
    color: var(--white); font-weight: 900; font-size: 92px; line-height: 1;
  }
  .total small { font-size: 62px; }
  .per-bottle {
    position: absolute; left: 0; width: 100%; text-align: center; top: 104px;
    color: var(--white); font-weight: 900; font-size: 44px; letter-spacing: 1px;
  }
  .count {
    position: absolute; left: 0; width: 100%; text-align: center; top: 160px;
    color: var(--ink); font-weight: 900; font-size: 40px; letter-spacing: 1px;
  }
  .net-weight {
    position: absolute; left: 126px; top: 215px; width: 309px; height: 42px;
    background: var(--white); border-radius: 21px;
    color: var(--ink); font-family: "Oswald", sans-serif; font-weight: 500; font-size: 30px;
    display: flex; align-items: center; justify-content: center;
  }
</style>
</head>
<body>
  <div class="label">
    <div class="top-band"><span class="tagline">OVERALL HEALTH &amp; WELNESS</span></div>

    <div class="body-panel" role="img" aria-label="Soft icy faceted background">
      <svg class="ring" width="860" height="682" viewBox="0 0 860 682">
        <circle cx="433" cy="531" r="310" fill="none" stroke="var(--ring)" stroke-width="4"/>
      </svg>
      <div class="brand">
        <span class="brand-dot"></span>
        <span class="brand-name">R4 Pips</span>
      </div>
    </div>

    <div class="product-title cbd">CBD</div>
    <div class="product-title gummies">GUMMIES</div>
    <div class="infused-bar">DELTA-8 INFUSED</div>
    <div class="dose-bar">15MG CBD PER GUMMIE</div>

    <div class="divider"></div>
    <div class="bottom-band">
      <div class="total">1500<small>MG</small></div>
      <div class="per-bottle">CBD PER BOTLE</div>
      <div class="count">100 COUNT</div>
      <div class="net-weight">NET WT 250G (8,8oz)</div>
    </div>
  </div>
</body>
</html>
```